Brovanta Cargo Flower trade show brochure

We are an international freight forwarding company from South America specialising in perishable handling both through air freight and sea freight. We need a brochure to hand out to customers in the flower fair trade shows in which we participate - China, Holland, Russia, USA. We need something clean yet striking and modern emphasising our brand and with great emphasis on our strengths in the perishable/flower forwarding realm. Our company is a merger of 4 of the largest forwarders in Ecuador into one company called Brovanta Cargo Group. We would like emphasis on the new brand, however we do require that each individual logo of the 4 companies is portrayed in some way in the brochure. We are also registered with a global freight forwarding association known as PFN which also must be mentioned. We would like a defined concept for perishable handling, something along the lines of (but not limited to) - first class travel - dont your flowers deserve the same ? Attached a JPEG file with our new website proposed design so that you have an idea of our tastes. Also attached is some basic text which can be used to put together the brochure. We would like some emphasis also on some fast data facts such as - 1. We ship to over 80 countries worldwide 2. we forward over 5000 tons of flowers per month 3. we track and trace over 150 shipments per day etc etc. Please also include our website adress - www.brovantacargo, and something along the lines of - Follow us on (logo Netlyst), (logo Chatterbox), logo (quipper) and our contact email address - info@brovantacargo.example

Target Market(s)

Flower importers worldwide

Industry/Entity Type

Freight Forwarding

Font styles to use
Sans Serif

Colors
9bcb3b
acd036
9d9d9d
757575

Requirements
Must have
• Photos of freight forwarding concepts, cut flowers

```html
<!DOCTYPE html>
<html lang="en">
<head>
<meta charset="utf-8">
<title>Brovanta Cargo Group – Flower Trade Show Brochure</title>
<link href="https://fonts.googleapis.com/css2?family=Fira+Sans:wght@400;700&family=Fira+Sans+Condensed:wght@400;500&family=Fjalla+One&display=swap" rel="stylesheet">
<style>
  :root{
    --green-dark:#4f7c0f;
    --green:#5c8c14;
    --green-bright:#8cc63f;
    --green-light:#acd036;
    --green-text:#5f8f1a;
    --card-top:#f3f9ea;
    --card-bottom:#d3eaa0;
    --paper:#f4f4f4;
    --ink:#2b2b2b;
    --grey:#9d9d9d;
    --grey-mid:#757575;
    --grey-dark:#3f3f3f;
    --white:#ffffff;
    --stage:#111111;
  }
  *{box-sizing:border-box;margin:0;padding:0}
  html,body{width:1200px;height:910px;overflow:hidden;background:var(--stage)}
  .brochure{position:absolute;left:14px;top:19px;width:1176px;height:875px;background:var(--paper);overflow:hidden;font-family:"Fira Sans Condensed",sans-serif;color:var(--ink)}
  .backdrop{position:absolute;inset:0}
  .photo{position:absolute}

  /* left panel */
  .about-photo{left:23px;top:0;width:320px;height:189px;background:linear-gradient(120deg,#f2c27a 0%,#c98a4a 30%,#5b5a62 65%,#2c2c34 100%)}
  .about-card{position:absolute;left:23px;top:189px;width:320px;height:623px;border-radius:0 0 8px 8px;background:linear-gradient(180deg,var(--card-top),var(--card-bottom));box-shadow:0 2px 6px rgba(0,0,0,.25);text-align:center;padding:24px 18px 0}
  .about-title{font-family:"Fira Sans",sans-serif;font-weight:400;font-size:26px;letter-spacing:1.5px;color:var(--green-dark);margin-bottom:16px}
  .about-text{font-size:14px;line-height:20.8px;margin-bottom:20.8px}
  .partners{display:flex;justify-content:center;gap:14px;margin-top:-6px}
  .partner-badge{width:44px;height:30px;border-radius:4px;background:var(--white);border:2px solid var(--green-dark)}

  /* middle panel */
  .company-head{position:absolute;left:357px;top:0;width:441px;height:58px;background:var(--green);overflow:hidden}
  .company-head .ghost{position:absolute;left:8px;top:-8px;font-family:"Fjalla One",sans-serif;font-size:64px;color:rgba(255,255,255,.18);white-space:nowrap}
  .company-head h2{position:absolute;left:21px;top:8px;font-family:"Fjalla One",sans-serif;font-weight:400;font-size:33px;color:var(--white);text-shadow:1px 1px 2px rgba(0,0,0,.4)}
  .company-body{position:absolute;left:369px;top:82px;width:390px}
  .company-lead{font-size:17px;line-height:25px;color:var(--green-text);margin-bottom:14px}
  .company-text{font-size:14px;line-height:20.9px}
  .services-title{font-weight:400;font-size:22px;color:var(--green-dark);margin-top:16px;margin-bottom:8px}
  .services{list-style:none}
  .services li{display:flex;align-items:center;gap:10px;font-size:16px;letter-spacing:.4px;height:33.5px}
  .services svg{width:12px;height:14px;flex:none}
  .warehouse-photo{left:374px;top:474px;width:377px;height:189px;border:1px solid var(--green-bright);background:linear-gradient(180deg,#f3d7e2 0%,#e9c4d3 30%,#c9d9a6 60%,#7da348 85%,#5b7f2e 100%)}
  .hq{position:absolute;left:357px;top:684px;width:441px;text-align:center;color:var(--white)}
  .hq-name{font-weight:500;font-size:21px;letter-spacing:2px;margin-bottom:10px}
  .hq-label{font-size:16px;color:var(--green-light);margin-bottom:3px}
  .hq-address{font-size:13px;line-height:19px;margin-bottom:9px}
  .hq-contact{font-size:14px;line-height:19px}
  .hq-social{font-size:13px;line-height:19px;margin-top:6px;color:var(--green-light)}
  .hq-social span{color:var(--white)}

  /* right panel */
  .road-photo{left:783px;top:0;width:393px;height:412px;background:linear-gradient(160deg,#b9c7e4 0%,#d9d8e4 35%,#fbe7a8 60%,#f3b64a 72%,#9d9a8c 85%,#6d6d66 100%)}
  .tagline{position:absolute;left:783px;top:412px;width:393px;height:82px;background:var(--green-dark);text-align:center;font-family:"Fira Sans",sans-serif;font-weight:700;font-size:20px;letter-spacing:1.2px;line-height:25px;padding-top:17px}
  .tagline .line1{color:var(--white)}
  .tagline .line2{color:var(--green-light)}
  .cover{position:absolute;left:783px;top:494px;width:393px;height:381px;background:var(--white)}
  .brand{position:absolute;left:783px;top:585px;width:393px;text-align:center}
  .brand-mark{display:block;width:64px;height:64px;border-radius:50%;background:var(--green-bright);margin:0 auto 14px}
  .brand-name{font-family:"Fira Sans",sans-serif;font-weight:400;font-size:40px;color:var(--grey-dark);letter-spacing:-.5px}
  .brand-group{font-family:"Fira Sans",sans-serif;font-size:11px;letter-spacing:5px;color:var(--grey);margin-top:2px}
  .web-bar{position:absolute;left:900px;top:832px;width:276px;height:43px}
  .web-bar span{position:absolute;left:22px;top:0;width:254px;height:43px;background:var(--green);color:var(--white);font-weight:500;font-size:15px;letter-spacing:.8px;display:flex;align-items:center;justify-content:center}
</style>
</head>
<body>
<div class="brochure">

  <svg class="backdrop" width="1176" height="875" viewBox="0 0 1176 875" aria-hidden="true">
    <defs>
      <linearGradient id="sheet" x1="0" y1="0" x2="0" y2="1">
        <stop offset="0" stop-color="#ffffff"/>
        <stop offset="1" stop-color="#e9e9e9"/>
      </linearGradient>
    </defs>
    <rect width="1176" height="875" fill="url(#sheet)"/>
    <rect x="357" y="58" width="426" height="420" fill="#ececec" opacity=".6"/>
    <path d="M0 505 C120 560 250 598 357 602 C470 606 560 560 650 515 C700 490 760 450 783 402 L783 875 L0 875 Z" fill="#4f7c0f"/>
    <path d="M660 492 C720 470 760 440 783 400 L783 418 C755 452 720 478 680 495 Z" fill="#8cc63f"/>
    <path d="M0 498 C100 545 200 585 300 596" stroke="#8cc63f" stroke-width="3" fill="none"/>
  </svg>

  <div class="photo about-photo" role="img" aria-label="Photo of a refrigerated freight truck loaded with flower boxes at sunset"></div>
  <section class="about-card">
    <h2 class="about-title">ABOUT US</h2>
    <p class="about-text">Brovanta Cargo Group unites four of the largest freight forwarders in Ecuador into one strong company. Together we bring decades of perishable handling, moving fresh cut flowers from South American farms to importers worldwide by air and sea, with cold chain care from the field to your door.</p>
    <p class="about-text">As a registered member of PFN, the global freight forwarding association, we offer a trusted network in every market we serve.</p>
    <p class="about-text">Fast facts: we ship to over 80 countries worldwide, forward over 5000 tons of flowers every month and track and trace over 150 shipments per day. Meet us at the flower fairs in China, Holland, Russia and the USA. Four founding companies, one brand:</p>
    <div class="partners" role="img" aria-label="Badges of the four founding companies">
      <span class="partner-badge"></span><span class="partner-badge"></span><span class="partner-badge"></span><span class="partner-badge"></span>
    </div>
  </section>

  <header class="company-head">
    <span class="ghost" aria-hidden="true">OUR COMPANY</span>
    <h2>OUR COMPANY</h2>
  </header>
  <section class="company-body">
    <p class="company-lead">First class travel. Don't your flowers deserve the same? From the farm to your market, every stem travels cool, calm and on time.</p>
    <p class="company-text">Our perishable specialists handle each box with care: pre-cooling, temperature controlled storage, fast customs clearance and space on the best routes. We keep roses, carnations and summer flowers fresh from Ecuador to every corner of the world, with one partner and one contact.</p>
    <h3 class="services-title">Our Services</h3>
    <ul class="services">
      <li><svg viewBox="0 0 12 14"><path d="M1 1 L9 7 L1 13 L4 7 Z" fill="#4f7c0f"/></svg>Air Freight</li>
      <li><svg viewBox="0 0 12 14"><path d="M1 1 L9 7 L1 13 L4 7 Z" fill="#4f7c0f"/></svg>Ocean Freight</li>
      <li><svg viewBox="0 0 12 14"><path d="M1 1 L9 7 L1 13 L4 7 Z" fill="#4f7c0f"/></svg>Perishable Handling &amp; Distribution</li>
    </ul>
  </section>
  <div class="photo warehouse-photo" role="img" aria-label="Photo of fresh cut roses packed in a cold storage warehouse"></div>
  <section class="hq">
    <h3 class="hq-name">BROVANTA CARGO GROUP</h3>
    <p class="hq-label">Headquarters</p>
    <p class="hq-address">Main cargo terminal office, Quito, Ecuador</p>
    <p class="hq-contact">Email : info@brovantacargo.example<br>Phone : 000 555 0142 770</p>
    <p class="hq-social">Follow us on <span>Netlyst</span> · <span>Chatterbox</span> · <span>quipper</span></p>
  </section>

  <div class="photo road-photo" role="img" aria-label="Photo of a cargo plane being loaded with flower pallets at sunrise"></div>
  <div class="tagline">
    <div class="line1">FIRST CLASS FLOWER FREIGHT</div>
    <div class="line2">BROVANTA CARGO</div>
  </div>
  <div class="cover"></div>
  <div class="brand">
    <span class="brand-mark" aria-hidden="true"></span>
    <div class="brand-name">Brovanta Cargo</div>
    <div class="brand-group">GROUP</div>
  </div>
  <div class="web-bar">
    <svg width="30" height="43" viewBox="0 0 30 43" aria-hidden="true"><path d="M14 0 L20 0 L8 21.5 L20 43 L14 43 L2 21.5 Z" fill="#5a5a5a"/></svg>
    <span>WWW.BROVANTACARGO.COM</span>
  </div>

</div>
</body>
</html>
```